Design for company homepage promoting to the pharmaceutical industry

Our company produces medical education materials and services for the pharmaceutical industry. Our existing website (www.quorvan.net.au) provides more information.
 
We need a homepage design for our new company website we are creating. Our site will not have a great amount of content, we want it to be fast, user friendly and easily adaptable to viewing on any platform, and through any browser. We don't want it over-designed - i.e. no highly animated banner flags, backgrounds, obscure webfonts, too many graphics etc. Attached are files indicating our existing company logo and design. We want the logo and rings to be retained. We've also attached draft copy for the website.
The final website may be designed in Wordpress (still to be confirmed)
 
This is a design to replace the current site (www.quorvan.net.au). Content will also be revised.
Things we don't like about our current design - doesn't use our current branding, is not very exciting, old fashioned 'standard' format, too much content, just doesn't look that good, boring.
 
Examples of sites we like:
www.brelmot.com.au
http://factsheets.wondipaq.com.au/index.html
 
Features we like from these sites - fast, responsive, short and to the point, cross-platform compatible including smartphones, and looks good
 
Main reasons people will visit our site: to find out whether we can provide services they might be looking for, to make a decision on whether they are interested in what we offer so they can get in touch with us, and to get our contact details.
Main thing we want to achieve from website visits is that it looks good enough and provides enough summary information on us so that they want to get in touch with us, to offer us work or to ask us to come in and meet them to provide more info on what we do.
Two most important calls to action from our website
· make the decision that we can do what you are looking for
· get in touch with us.
Updates

Thanks everyone for your submissions. At this stage with the Christmas break upon us, we are yet to finalise our decision, and will make a decision early in the new year. I hope everyone has a good holiday break.
Kind regards
Doug

Target Market(s)

Pharmaceutical industry professionals, marketers and medical professionals.

Industry/Entity Type

Pharmaceutical

Requirements
Must have
• Company logo and rings must be incorporated, company colour - blue - must be in there.
Should not have
• Complex animation or graphics that will slow the upload or limit cross-platform compatability/viewing on smartphones etc.

```html
<!DOCTYPE html>
<html lang="en">
<head>
<meta charset="utf-8">
<title>Quorvan Healthcare Education</title>
<link rel="stylesheet" href="https://fonts.googleapis.com/css2?family=Open+Sans:wght@400;600&family=Questrial&family=Arimo:wght@400;700&display=swap">
<style>
:root{
  --blue:#1a6fb5;
  --blue-bright:#1296e0;
  --nav-bg:#d9ecf7;
  --band-bg:#bde0f2;
  --text:#4a4a4a;
  --panel:#eef2f5;
  --footer:#7eb0da;
  --footer-dark:#5f98cf;
  --white:#ffffff;
}
*{box-sizing:border-box;margin:0;padding:0}
html,body{width:814px;height:1200px;overflow:hidden;background:var(--white)}
body{font-family:"Open Sans",sans-serif;color:var(--text);position:relative}
.site-header{height:177px;display:flex;align-items:center;justify-content:center}
.brand{display:flex;align-items:center;gap:8px;font-family:"Open Sans",sans-serif;font-weight:400;font-size:50px;color:var(--blue);letter-spacing:1px;margin-top:-40px}
.brand-dot{width:8px;height:8px;border-radius:50%;background:var(--blue);opacity:.6}
.main-nav{height:35px;background:var(--nav-bg);display:flex;align-items:center}
.main-nav a{font-size:12.5px;color:var(--blue);text-decoration:none;height:35px;line-height:35px;padding:0 0 0 0;text-align:center}
.main-nav a.active{background:var(--blue-bright);color:var(--white);width:87px}
.main-nav .links{display:flex;flex:1;justify-content:space-around}
.hero{height:294px;background:linear-gradient(180deg,#1e5a9a 0%,#3b7fc0 38%,#c9d6e2 62%,#eef1f4 100%)}
.services{height:182px;background:var(--band-bg);display:flex;padding:22px 0 0 12px}
.service{width:163px;padding-right:8px}
.service-icon{width:64px;height:64px;border-radius:50%;background:#e6f3fb;margin:0 0 0 53px;display:flex;align-items:center;justify-content:center}
.service-icon svg{width:34px;height:34px;fill:var(--blue)}
.service h3{font-family:"Questrial",sans-serif;font-weight:400;font-size:15.5px;color:var(--blue);text-align:center;margin:22px 0 6px;text-transform:uppercase}
.service p{font-size:10px;line-height:1.02;color:var(--blue)}
.content{height:318px;position:relative}
.intro{position:absolute;left:17px;top:20px;width:470px}
.intro h1{font-family:"Questrial",sans-serif;font-weight:400;font-size:19px;line-height:20px;color:var(--blue-bright);letter-spacing:-.6px;margin-bottom:12px}
.intro p{font-size:11.6px;line-height:14px;margin-bottom:18px}
.intro ul{list-style:none}
.intro li{font-size:11.6px;line-height:11.8px;padding-left:32px;position:relative;margin-bottom:11px}
.intro li::before{content:"";position:absolute;left:10px;top:3px;width:8px;height:8px;border-radius:50%;background:#555}
.contact-panel{position:absolute;left:545px;top:17px;width:259px;height:265px;background:var(--panel);padding:16px 19px}
.contact-panel h2{font-family:"Questrial",sans-serif;font-weight:400;font-size:15.5px;color:var(--blue-bright);margin-bottom:8px;letter-spacing:-.3px}
.field{background:var(--white);border:1px solid #dde3e8;height:27px;margin-bottom:6px;font-family:"Arimo",sans-serif;font-size:10px;color:#8a9aa8;padding:8px}
.field.message{height:84px}
.submit{display:inline-block;background:var(--blue-bright);color:var(--white);font-family:"Arimo",sans-serif;font-size:10.5px;width:89px;height:25px;line-height:25px;text-align:center;margin-top:4px}
.site-footer{height:171px;background:var(--footer);position:relative;color:var(--white);font-family:"Arimo",sans-serif}
.site-footer h4{font-family:"Questrial",sans-serif;font-weight:400;font-size:15.5px;letter-spacing:-.3px;text-transform:uppercase}
.foot-nav{position:absolute;left:13px;top:28px}
.foot-nav .cols{display:flex;gap:0;margin-top:11px}
.foot-nav ul{list-style:none;width:83px}
.foot-nav li{font-size:10px;line-height:13.3px}
.foot-quote{position:absolute;left:274px;top:28px;width:280px}
.quote-body{display:flex;gap:12px;margin-top:10px}
.quote-body svg{flex:none;width:38px;height:36px}
.foot-quote p{font-size:10px;line-height:12px}
.foot-quote .second{margin-top:9px}
.connect{position:absolute;left:616px;top:28px;width:190px}
.social{display:flex;gap:8px;margin:12px 0 10px}
.social span{width:23px;height:23px;border-radius:50%;background:var(--white)}
.connect .note{font-size:8.8px;line-height:11px}
.email{background:var(--white);border-radius:12px;width:153px;height:23px;margin:7px 0 8px -2px;color:var(--blue);font-size:9px;line-height:23px;padding-left:12px}
.subscribe{font-size:9px;font-weight:700;display:flex;align-items:center;gap:6px}
.copyright{height:23px;background:var(--footer-dark);color:var(--white);font-family:"Arimo",sans-serif;font-size:9px;line-height:23px;padding-left:14px}
</style>
</head>
<body>
<header class="site-header">
  <div class="brand"><span>quorvan</span><span class="brand-dot"></span></div>
</header>

<nav class="main-nav">
  <a class="active" href="#">Home</a>
  <div class="links">
    <a href="#">Who We Are</a><a href="#">What We Do</a><a href="#">Clients</a><a href="#">Work</a><a href="#">Testimonials</a><a href="#">Contact Us</a><a href="#">Login</a>
  </div>
</nav>

<div class="hero" role="img" aria-label="Photo of a stethoscope resting on an open medical book against a blue background"></div>

<section class="services">
  <div class="service">
    <div class="service-icon"><svg viewBox="0 0 34 34"><rect x="6" y="7" width="22" height="15" rx="2"/><rect x="3" y="23" width="28" height="3" rx="1"/></svg></div>
    <h3>Promotion</h3>
    <p>Quorvan can help you promote your brand – from the development of strategic communication campaigns .</p>
  </div>
  <div class="service">
    <div class="service-icon"><svg viewBox="0 0 34 34"><rect x="15" y="3" width="5" height="14" rx="1" transform="rotate(-30 17 10)"/><path d="M8 30h18v-3H19c3-2 5-5 4-9l-3 1c1 3-1 6-4 8H8z"/><rect x="11" y="18" width="6" height="3"/></svg></div>
    <h3>Education</h3>
    <p>Clinical papers, evidence summaries, scientific newsletters and accredited educational materials.</p>
  </div>
  <div class="service">
    <div class="service-icon"><svg viewBox="0 0 34 34"><rect x="4" y="4" width="14" height="6"/><rect x="4" y="12" width="14" height="6"/><rect x="4" y="20" width="14" height="8"/><rect x="18" y="16" width="12" height="12"/></svg></div>
    <h3>Programs</h3>
    <p>From clinical audits to patient support activities, Quorvan has successfully develop and complex program.</p>
  </div>
  <div class="service">
    <div class="service-icon"><svg viewBox="0 0 34 34"><circle cx="10" cy="11" r="4"/><circle cx="24" cy="11" r="4"/><circle cx="17" cy="14" r="4.5"/><path d="M3 26c0-5 3-9 7-9s7 4 7 9z"/><path d="M17 26c0-5 3-9 7-9s7 4 7 9z"/><path d="M9 29c0-6 4-10 8-10s8 4 8 10z"/></svg></div>
    <h3>Meetings</h3>
    <p>You will maximise your investment in scientific meetings by employing Quorvan to manage the entire process.</p>
  </div>
  <div class="service">
    <div class="service-icon"><svg viewBox="0 0 34 34"><path d="M13 8h8v2h-1v6l7 12H7l7-12v-6h-1z"/><circle cx="17" cy="3" r="1.5"/></svg></div>
    <h3>IME</h3>
    <p>In an environment of ever-increasing scrutiny over the support that pharmaceutical companies.</p>
  </div>
</section>

<section class="content">
  <div class="intro">
    <h1>At Quorvan we are healthcare communication specialists; this means we’re scientists, journalists and marketers rolled into one.</h1>
    <p>As you can see we provide all the things you’d expect from a top-class healthcare communications agency, but we have the depth of technical understanding and creative flair to produce sophisticated and memorable materials and programs, including:</p>
    <ul>
      <li>Strategic tools for brand promotion (such as detail aids, product monographs, slide kits and patient materials)</li>
      <li>Non-promotional materials for market education (e.g. clinical papers and evidence summaries)</li>
      <li>Complex programs such as clinical audits and product familiarisation programs</li>
      <li>Medical meetings and symposia</li>
    </ul>
  </div>
  <aside class="contact-panel">
    <h2>CONTACT US</h2>
    <div class="field">Full Name</div>
    <div class="field">Email</div>
    <div class="field">Telephone</div>
    <div class="field message">Message</div>
    <div class="submit">Submit</div>
  </aside>
</section>

<footer class="site-footer">
  <div class="foot-nav">
    <h4>Navigation</h4>
    <div class="cols">
      <ul><li>Home</li><li>Who We Are</li><li>What We Do</li><li>Clients</li><li>Work</li><li>Testimonials</li></ul>
      <ul><li>Contact Us</li><li>Login</li><li>Privacy Policy</li><li>Terms of Use</li></ul>
    </div>
  </div>
  <div class="foot-quote">
    <h4>Testimonial</h4>
    <div class="quote-body">
      <svg viewBox="0 0 38 36" fill="none" stroke="#fff" stroke-width="2"><ellipse cx="15" cy="14" rx="13" ry="11"/><path d="M8 23l-3 7 8-5"/><ellipse cx="27" cy="24" rx="9" ry="8" fill="#fff"/></svg>
      <p>“Congratulations &amp; many thanks for your seriously wonderful &amp; successful work on the weekend. I’m especially grateful for the calm, cool &amp; very clever work done in managing all the planning process before I even came on board – truly outstanding”</p>
    </div>
    <p class="second">“Thank you for all your help with making the meeting the huge success that it was”</p>
  </div>
  <div class="connect">
    <h4>Connect With Us</h4>
    <div class="social"><span></span><span></span><span></span><span></span><span></span></div>
    <p class="note">subscribe to our monthly newsletter and get the best deals and discounts</p>
    <div class="email">enter email address</div>
    <div class="subscribe"><svg width="8" height="8" viewBox="0 0 8 8"><path d="M0 0l8 4-8 4 2-4z" fill="#fff"/></svg>subscribe now</div>
  </div>
</footer>
<div class="copyright">© Copyright 2013 Quorvan. All Rights Reserved</div>
</body>
</html>
```